以下のイメージでデザインをお願いいたします。
ご提案の際には、デザインに込めた意味合いも、お書き添えいただけるとうれしいです。

・シンプル、かつスタイリッシュ、また、親しみやすさがありながらも、品格があるデザイン
・アフリカのポップアートも扱いますが、事業内容は多岐に渡るため、ポップな感じだけの名刺はNG
・名刺の向きはタテ型でも横型でもOK
・「会社として大事にしていることや目標」に加えて、「成長していく」、「飛躍する」イメージを込めていただいたデザイン
・名刺を配布する先はBtoBで、当面は日本の企業様が対象
⇒CSR(社会貢献活動)に力をいれている企業や消費財を扱う企業の方々に訴求していきたいと思っています。
企業の担当者としてはマーケティングや営業関係、役員クラス、経営者などを想定しています。
・印刷用紙はマット系
■表面(日本語):名前(ダミー)、肩書き(CEO & Co-Founder)、会社名、住所(ダミー)、HP URL(ダミー)、e-mail(ダミー)、携帯電話番号(ダミー)

■裏面(英語):名前(ダミー)、肩書き(CEO & Co-Founder)、会社名、住所(ダミー)、HP URL(ダミー)、e-mail(ダミー)、携帯電話番号(ダミー 、+81を付けてください)
ロゴにあるオレンジ、グレー、白の3色を使用する
▼事業内容
・デジタルコンテンツの企画・制作及び販売・輸出入
・絵画その他美術品等の販売及び輸出入
・ライセンス管理及びライセンス許諾事業
・学術、文化、芸術又はスポーツの振興を図る活動
このたびは、弊社の名刺コンペにご参加いただきありがとうございます。
たくさんの素晴らしいご提案をいただき、感謝しております。
これから選定に入らせていただきたいと思います。年末年始をはさみますので、恐れ入りますが、1月4日頃を目処に発表させていただきたく存じます。
ご参加いただいたデザイナー、クリエイターの皆様に重ねて御礼申し上げます。
どうぞ良い年をお迎えくださいませ。

金賞:morning57様
シンプルで飽きのこないデザインで、ロゴと社名のバランスが絶妙でした。また、裏面も表とは違う表情を演出してあり好感をもちました。

銀賞:
r-opa様
透かし模様のロゴが秀逸でした。裏面は色合いを変えてくださったバージョンが素敵でした。

hiroe48様
パズルのピース部分を抜き出した使い方が個性的でインパクトがありました。

このたびは、弊社の名刺コンペにご参加いただきありがとうございました。
ロゴを活かしてくださるすばらしいデザインばかりで、提案をいただくのがとても楽しみでした。
全てのご提案にコメントをお返ししきれず、心苦しいかぎりです。
今後も、デザイン募集の依頼をさせていただくことがあるかと存じますが、ぜひまた応募をいただければ幸いです。
応募いただいたデザイナーの皆様に、この場を借りて、改めて御礼申し上げます。今後ともよろしくお願い申し上げます。

```html
<!DOCTYPE html>
<html lang="ja">
<head>
<meta charset="utf-8">
<title>Maretta Holdings – Business Card</title>
<link href="https://fonts.googleapis.com/css2?family=Noto+Sans+JP:wght@400;500;700&display=swap" rel="stylesheet">
<style>
  :root {
    --stage: #d9d9d9;
    --label: #ffffff;
    --card: #ffffff;
    --orange: #e8702a;
    --orange-deep: #de6420;
    --ink: #3d3d3d;
    --gray: #6b6b6b;
    --pattern-light: #e3e9ef;
    --white: #ffffff;
  }
  * { margin: 0; padding: 0; box-sizing: border-box; }
  html, body { width: 800px; height: 1200px; overflow: hidden; }
  body {
    background: var(--stage);
    font-family: "Noto Sans JP", sans-serif;
    color: var(--ink);
    position: relative;
  }
  .side-label {
    position: absolute;
    left: 48px;
    font-size: 22px;
    color: var(--label);
    font-weight: 400;
  }
  .side-label.front { top: 64px; }
  .side-label.back { top: 628px; }

  .card {
    position: absolute;
    left: 110px;
    width: 676px;
    height: 409px;
    background: var(--card);
    overflow: hidden;
    box-shadow: 0 2px 6px rgba(0,0,0,0.18);
  }
  .card.front { top: 118px; }
  .card.back { top: 680px; }

  .pattern-strip {
    position: absolute; left: 0; top: 0;
    width: 107px; height: 245px;
    background: var(--pattern-light);
  }
  .pattern-strip.on-band {
    top: 245px; height: 164px;
    background: var(--orange-deep);
  }
  .band {
    position: absolute; left: 0; top: 245px;
    width: 100%; height: 164px;
    background: var(--orange);
  }

  .brand {
    position: absolute; right: 28px; top: 30px;
    display: flex; align-items: center; gap: 12px;
  }
  .brand-dot { width: 44px; height: 44px; border-radius: 50%; background: var(--orange); }
  .brand-name {
    font-weight: 700; color: var(--gray);
    font-size: 26px; line-height: 1.1;
  }
  .brand-name small { display: block; font-size: 17px; }

  .person { position: absolute; left: 125px; top: 128px; }
  .title { font-size: 15px; color: var(--ink); }
  .name-jp { font-size: 38px; font-weight: 500; letter-spacing: 6px; margin-top: 4px; }
  .name-jp .roman { font-size: 14px; letter-spacing: 0; margin-left: 8px; }
  .name-en { font-size: 40px; font-weight: 500; margin-top: 2px; }
  .mobile { display: flex; align-items: center; gap: 6px; font-size: 17px; margin-top: 2px; }

  .contact {
    position: absolute; left: 125px; top: 260px;
    color: var(--white); font-size: 15px; line-height: 27px;
  }
  .contact .company { font-size: 17px; font-weight: 500; }
  .row { display: flex; align-items: flex-start; gap: 6px; }
  .row .ico { margin-top: 6px; flex: none; }
  .ico { width: 15px; height: 15px; display: inline-block; }

  .contact.en { top: 254px; line-height: 24px; }
  .contact.en .company { font-size: 22px; font-weight: 700; line-height: 30px; }
  .contact.en .row .ico { margin-top: 4px; }
  .address-en { line-height: 19px; padding: 2px 0 3px; }
  .address-en .ico { margin-top: 2px !important; }
</style>
</head>
<body>

<div class="side-label front">Front</div>
<section class="card front">
  <div class="pattern-strip" role="img" aria-label="Faint repeating company symbol pattern"></div>
  <div class="band"></div>
  <div class="pattern-strip on-band" role="img" aria-label="Tone-on-tone repeating company symbol pattern"></div>

  <div class="brand">
    <span class="brand-dot"></span>
    <span class="brand-name">Maretta<small>Holdings Co.,Ltd.</small></span>
  </div>

  <div class="person">
    <p class="title">CEO</p>
    <p class="name-jp">森川 陽介<span class="roman">Yosuke Morikawa</span></p>
    <p class="mobile">
      <svg class="ico" viewBox="0 0 16 16"><rect width="16" height="16" rx="2" fill="#6b6b6b"/><rect x="5" y="2.5" width="6" height="11" rx="1" fill="none" stroke="#fff" stroke-width="1.3"/></svg>
      090-1111-2222
    </p>
  </div>

  <div class="contact">
    <p class="company">株式会社マレッタ・ホールディングス</p>
    <p class="row">
      <svg class="ico" viewBox="0 0 16 16"><rect width="16" height="16" rx="2" fill="#fff"/><path d="M8 3a3.5 3.5 0 0 0-3.5 3.5C4.5 9 8 13 8 13s3.5-4 3.5-6.5A3.5 3.5 0 0 0 8 3z" fill="#e8702a"/></svg>
      〒123-4567 東京都港区青葉台1-2-34 青葉ビル2F
    </p>
    <p class="row">
      <svg class="ico" viewBox="0 0 16 16"><rect width="16" height="16" rx="2" fill="#fff"/><path d="M5 3.5l2 2-1.2 1.3a7 7 0 0 0 3.4 3.4L10.5 9l2 2-1.5 1.5C7 12.5 3.5 9 3.5 5z" fill="#e8702a"/></svg>
      03-1111-3333
      <svg class="ico" viewBox="0 0 16 16"><rect width="16" height="16" rx="2" fill="#fff"/><rect x="3" y="6" width="10" height="6" fill="#e8702a"/><rect x="5" y="3" width="6" height="3" fill="#e8702a"/></svg>
      03-1111-3333
    </p>
    <p class="row">
      <svg class="ico" viewBox="0 0 16 16"><rect width="16" height="16" rx="2" fill="#fff"/><rect x="3" y="4.5" width="10" height="7" fill="none" stroke="#e8702a" stroke-width="1.3"/><path d="M3 4.5l5 4 5-4" fill="none" stroke="#e8702a" stroke-width="1.3"/></svg>
      hello@maretta.example
    </p>
    <p class="row">
      <svg class="ico" viewBox="0 0 16 16"><circle cx="8" cy="8" r="7.5" fill="#fff"/><circle cx="8" cy="8" r="5" fill="none" stroke="#e8702a" stroke-width="1.2"/><path d="M3 8h10M8 3c-2 2.5-2 7.5 0 10M8 3c2 2.5 2 7.5 0 10" fill="none" stroke="#e8702a" stroke-width="1"/></svg>
      http://www.maretta.example
    </p>
  </div>
</section>

<div class="side-label back">Back</div>
<section class="card back">
  <div class="pattern-strip" role="img" aria-label="Faint repeating company symbol pattern"></div>
  <div class="band"></div>
  <div class="pattern-strip on-band" role="img" aria-label="Tone-on-tone repeating company symbol pattern"></div>

  <div class="brand">
    <span class="brand-dot"></span>
    <span class="brand-name">Maretta<small>Holdings Co.,Ltd.</small></span>
  </div>

  <div class="person">
    <p class="title">CEO</p>
    <p class="name-en">Yosuke Morikawa</p>
    <p class="mobile">
      <svg class="ico" viewBox="0 0 16 16"><rect width="16" height="16" rx="2" fill="#6b6b6b"/><rect x="5" y="2.5" width="6" height="11" rx="1" fill="none" stroke="#fff" stroke-width="1.3"/></svg>
      090-1111-2222
    </p>
  </div>

  <div class="contact en">
    <p class="company">Maretta Holdings Co.,Ltd.</p>
    <p class="row address-en">
      <svg class="ico" viewBox="0 0 16 16"><rect width="16" height="16" rx="2" fill="#fff"/><path d="M8 3a3.5 3.5 0 0 0-3.5 3.5C4.5 9 8 13 8 13s3.5-4 3.5-6.5A3.5 3.5 0 0 0 8 3z" fill="#e8702a"/></svg>
      <span>Aoba Bld 2F,1-2-34, Aobadai,Minato-ku,<br>Tokyo,123-0000, Japan</span>
    </p>
    <p class="row">
      <svg class="ico" viewBox="0 0 16 16"><rect width="16" height="16" rx="2" fill="#fff"/><path d="M5 3.5l2 2-1.2 1.3a7 7 0 0 0 3.4 3.4L10.5 9l2 2-1.5 1.5C7 12.5 3.5 9 3.5 5z" fill="#e8702a"/></svg>
      +81-3-1111-3333
      <svg class="ico" viewBox="0 0 16 16"><rect width="16" height="16" rx="2" fill="#fff"/><rect x="3" y="6" width="10" height="6" fill="#e8702a"/><rect x="5" y="3" width="6" height="3" fill="#e8702a"/></svg>
      +81-3-1111-3333
    </p>
    <p class="row">
      <svg class="ico" viewBox="0 0 16 16"><rect width="16" height="16" rx="2" fill="#fff"/><rect x="3" y="4.5" width="10" height="7" fill="none" stroke="#e8702a" stroke-width="1.3"/><path d="M3 4.5l5 4 5-4" fill="none" stroke="#e8702a" stroke-width="1.3"/></svg>
      hello@maretta.example
    </p>
    <p class="row">
      <svg class="ico" viewBox="0 0 16 16"><circle cx="8" cy="8" r="7.5" fill="#fff"/><circle cx="8" cy="8" r="5" fill="none" stroke="#e8702a" stroke-width="1.2"/><path d="M3 8h10M8 3c-2 2.5-2 7.5 0 10M8 3c2 2.5 2 7.5 0 10" fill="none" stroke="#e8702a" stroke-width="1"/></svg>
      http://www.maretta.example
    </p>
  </div>
</section>

</body>
</html>
```